we are in the infrastructure business ( road construction ) and I need a billboard that I placed it at every project to illustrate that we worked there . We have the logo , I attached it , I just need an interesting design of the billboard.
The company s name is : Vextra Civil - I attached how to be written !
I don't need to write road construction business on it

Requirements
Must have
• Study the design of the logo I attached ( the sign with " KTP " is just an example !!
Nice to have
• the romanian flag but made into a special form ( I attached an Idea )

```html
<!DOCTYPE html>
<html lang="en">
<head>
<meta charset="utf-8">
<title>Vextra Civil – Project Billboard</title>
<link rel="stylesheet" href="https://fonts.googleapis.com/css2?family=League+Spartan:wght@600&display=swap">
<style>
  :root {
    --navy: #2e3a48;
    --sky-blue: #63bbe7;
    --stage: #e9ecef;
    --sky-top: #6f9fae;
    --sky-warm: #d9a27a;
    --haze: #c9c3bb;
    --road: #4a4b4f;
    --road-dark: #2b2c30;
    --flag-blue: #2b3a8f;
    --flag-yellow: #f5d21a;
    --flag-red: #d6262b;
  }
  * { margin: 0; padding: 0; box-sizing: border-box; }
  html, body {
    width: 1200px;
    height: 510px;
    overflow: hidden;
    background: var(--stage);
  }
  .canvas {
    width: 1200px;
    height: 510px;
    display: flex;
    align-items: center;
    justify-content: center;
  }
  .billboard {
    display: block;
    width: 679px;
    height: 510px;
  }
  .wordmark {
    font-family: "League Spartan", "Helvetica Neue", Arial, sans-serif;
    font-weight: 600;
    fill: var(--navy);
  }
</style>
</head>
<body>
<main class="canvas">
  <svg class="billboard" viewBox="0 0 1456 1094" xmlns="http://www.w3.org/2000/svg">
    <defs>
      <linearGradient id="site-photo-tone" x1="0" y1="0" x2="0" y2="1">
        <stop offset="0" stop-color="var(--sky-top)"/>
        <stop offset="0.3" stop-color="var(--sky-warm)"/>
        <stop offset="0.5" stop-color="var(--haze)"/>
        <stop offset="0.62" stop-color="var(--road)"/>
        <stop offset="1" stop-color="var(--road-dark)"/>
      </linearGradient>
      <linearGradient id="flag-tone" x1="0" y1="0" x2="1" y2="0">
        <stop offset="0" stop-color="var(--flag-blue)" stop-opacity="0.85"/>
        <stop offset="0.33" stop-color="var(--flag-blue)"/>
        <stop offset="0.45" stop-color="var(--flag-yellow)"/>
        <stop offset="0.62" stop-color="var(--flag-yellow)"/>
        <stop offset="0.72" stop-color="var(--flag-red)"/>
        <stop offset="1" stop-color="var(--flag-red)" stop-opacity="0.8"/>
      </linearGradient>
    </defs>

    <!-- base panel -->
    <rect class="panel-base" x="0" y="0" width="1456" height="1094" fill="var(--navy)"/>

    <!-- road works photo -->
    <polygon class="site-photo" role="img"
             aria-label="Photo of heavy trucks working on a new motorway under a warm sunset sky"
             points="730,0 1456,0 1456,1094 975,1094 1220,720 285,720"
             fill="url(#site-photo-tone)"/>

    <!-- darker corner overlay -->
    <polygon class="photo-shade" points="1456,360 1456,1094 975,1094" fill="var(--navy)" opacity="0.35"/>

    <!-- light blue divider stripe -->
    <polygon class="divider-stripe" points="678,0 730,0 285,720 243,720" fill="var(--sky-blue)"/>

    <!-- brand mark area -->
    <circle class="brand-ring" cx="245" cy="250" r="180" fill="none" stroke="var(--sky-blue)" stroke-width="22"/>

    <!-- name band -->
    <polygon class="name-band" points="0,720 1220,720 975,1094 0,1094" fill="var(--sky-blue)"/>

    <text class="wordmark wordmark-main" x="55" y="925" font-size="160" textLength="760" lengthAdjust="spacing">VEXTRA</text>
    <text class="wordmark wordmark-sub" x="625" y="1015" font-size="98" textLength="365" lengthAdjust="spacing">CIVIL</text>

    <!-- romanian flag splash -->
    <rect class="flag-splash" role="img"
          aria-label="Romanian flag in a painted splatter style"
          x="1160" y="790" width="260" height="240" rx="40"
          fill="url(#flag-tone)"/>
  </svg>
</main>
</body>
</html>
```